Business Card Design

I would like a logo created for the top left corner of the card please. I would like a checkerboard in a dark navy with the edges fading out and one random bright orange square.
Updates

I have attached some further notes and a really rough sketch of what I am after.  Thank you. :)

Target Market(s)

Construction, mining, mechanical

Industry/Entity Type

Business

Contact Information for Business Card

KRW Fabrications Pty Ltd, Oscar Plunkett, P. 0413658207, F. 0753917260, E.oscar@krwfabrications.com.au, PO Box 87 WONGARA Q 4571, ABN 52983470611

Font styles to use
Sans Serif

Requirements
Must have
• Really Dark Navy
Really bright Orange

```html
<!DOCTYPE html>
<html lang="en">
<head>
<meta charset="utf-8">
<title>KRW Fabrications Pty Ltd — Business Card</title>
<link rel="stylesheet" href="https://fonts.googleapis.com/css2?family=Lato:wght@400;700&display=swap">
<style>
  :root {
    --navy: #1b2142;
    --navy-soft: #2a3152;
    --orange: #ea5a1c;
    --card: #f1f1f1;
    --card-edge: #e2e2e2;
    --stage: #d9d6d1;
    --text: #2b2f45;
  }
  * { box-sizing: border-box; margin: 0; padding: 0; }
  html, body {
    width: 1200px;
    height: 1023px;
    overflow: hidden;
    background: var(--stage);
    font-family: "Lato", sans-serif;
  }
  .business-card {
    position: absolute;
    left: 150px;
    top: 254px;
    width: 900px;
    height: 514px;
    background: linear-gradient(160deg, #fafafa 0%, var(--card) 55%, var(--card-edge) 100%);
    box-shadow: 0 18px 40px rgba(0,0,0,0.25);
    overflow: hidden;
  }
  .brand {
    position: absolute;
    left: 60px;
    top: 70px;
    display: flex;
    align-items: center;
    gap: 18px;
  }
  .brand-square {
    width: 34px;
    height: 34px;
    background: var(--orange);
  }
  .brand-name {
    font-weight: 700;
    font-size: 40px;
    color: var(--navy);
    letter-spacing: 0.5px;
  }
  .contact-block {
    position: absolute;
    left: 60px;
    top: 250px;
    color: var(--text);
  }
  .person-name {
    font-size: 27px;
    font-weight: 400;
    letter-spacing: 1.5px;
    text-transform: uppercase;
    margin-bottom: 16px;
    color: var(--navy);
  }
  .contact-list { list-style: none; }
  .contact-item {
    display: flex;
    align-items: center;
    gap: 12px;
    font-size: 21px;
    line-height: 34px;
    letter-spacing: 0.5px;
  }
  .contact-icon { width: 20px; height: 20px; flex: none; }
  .contact-band {
    position: absolute;
    left: 0;
    right: 0;
    bottom: 0;
    height: 76px;
    background: linear-gradient(180deg, var(--navy-soft), var(--navy));
    border-top: 4px solid var(--orange);
    display: flex;
    align-items: center;
    justify-content: space-between;
    padding: 0 44px 0 60px;
    font-size: 21px;
    letter-spacing: 0.5px;
  }
  .postal-address { color: #ffffff; }
  .abn { color: var(--orange); }
</style>
</head>
<body>
  <main class="business-card">
    <div class="brand">
      <span class="brand-square"></span>
      <span class="brand-name">KRW Fabrications Pty Ltd</span>
    </div>

    <section class="contact-block">
      <h1 class="person-name">Oscar Plunkett</h1>
      <ul class="contact-list">
        <li class="contact-item">
          <svg class="contact-icon" viewBox="0 0 20 20" aria-hidden="true">
            <circle cx="10" cy="10" r="9" fill="none" stroke="#ea5a1c" stroke-width="1.6"/>
            <rect x="7" y="5" width="6" height="10" rx="1" fill="none" stroke="#ea5a1c" stroke-width="1.4"/>
          </svg>
          <span>0413658207</span>
        </li>
        <li class="contact-item">
          <svg class="contact-icon" viewBox="0 0 20 20" aria-hidden="true">
            <circle cx="10" cy="10" r="9" fill="none" stroke="#ea5a1c" stroke-width="1.6"/>
            <rect x="5.5" y="8" width="9" height="5" rx="1" fill="#ea5a1c"/>
            <rect x="7.5" y="5" width="5" height="3" fill="none" stroke="#ea5a1c" stroke-width="1.2"/>
            <rect x="7.5" y="12" width="5" height="3" fill="#fff" stroke="#ea5a1c" stroke-width="1.2"/>
          </svg>
          <span>0753917260</span>
        </li>
        <li class="contact-item">
          <svg class="contact-icon" viewBox="0 0 20 20" aria-hidden="true">
            <circle cx="10" cy="10" r="9" fill="none" stroke="#ea5a1c" stroke-width="1.6"/>
            <rect x="5" y="6.5" width="10" height="7" fill="#ea5a1c"/>
            <path d="M5 6.5 L10 10.5 L15 6.5" fill="none" stroke="#fff" stroke-width="1.2"/>
          </svg>
          <span>oscar@krwfabrications.com.au</span>
        </li>
      </ul>
    </section>

    <footer class="contact-band">
      <span class="postal-address">PO Box 87 WONGARA Q 4571</span>
      <span class="abn">ABN 52983470611</span>
    </footer>
  </main>
</body>
</html>
```